magcian / mentalist needs flyer desined to send potentisl clients

I need a design that's contemporary, sharp, fun, and professional that will get the attention of whoever receives the flyer very quickly. This is for a tri-fold flyer design.

I've been performing magic for over 40 years. I've performed close-up,
parlor, and stage shows. I've been an Master of Ceremonies, Key Note
Speaker (using magic during presentations to help build on a point or
topic, while keeping the audience entertained and educated on the topic or
topics the client has asked me to focus). I've worked trade shows and
sales training incorporating magic as well. I did private shows in Las
Vegas and L.A. back in the late 90's as well.

I do have website / wesleytorvandmagic.example for your to check out.

Target Market(s)

The target audience is corporation Event Planners, Marketing and Sales
managers, casino & hotel entertainment directors, as well as private
businesses looking for unique entertainment options.

Industry/Entity Type

Entertainment Industry

Logo Text

Here are a couple of ideas: your mind is my playground, neural entertainer, professor of mysteries, master of your mind

Requirements
Must have
• I like the black and white look (I think it looks nice, but open to other
• ideas and creativity. Being I'm a magician and mentalist, I'd like for
• both venues to be conveyed somehow. My magic is clean and corporate and family friendly.
Nice to have
• I do have website / wesleytorvandmagic.example for your to check out.
• My current business card is attached for review. I'll also attach photos
• I'd like to share, but was unable when I last attempted do sign up. Some
• of the files were too big and I'm not savvy enough to make them smaller,
• but think there might be some potential with a couple.
Should not have
• cartoons or cartoonish graphics. no rabbits, doves, magicians, wands, or top hats.

```html
<!DOCTYPE html>
<html lang="en">
<head>
<meta charset="utf-8">
<title>Wesley Torvand – Magician, Mentalist, Entertainer – Tri-fold</title>
<link rel="stylesheet" href="https://fonts.googleapis.com/css2?family=Open+Sans:wght@300;400;600;700&family=Shadows+Into+Light&display=swap">
<style>
  :root {
    --backdrop: #cfcfcf;
    --frame-line: #8a8a8a;
    --ink: #050505;
    --paper: #ffffff;
    --soft-white: #ececec;
    --quote-mark: #8f8f8f;
  }
  * { margin: 0; padding: 0; box-sizing: border-box; }
  html, body { width: 1200px; height: 885px; overflow: hidden; }
  body {
    background: var(--backdrop);
    font-family: "Open Sans", Arial, sans-serif;
    position: relative;
  }
  .stage-frame {
    position: absolute;
    left: 11px; top: 5px; width: 1173px; height: 875px;
    border: 1px solid var(--frame-line);
    background: #d4d4d4;
  }
  .trifold {
    position: absolute;
    left: 57px; top: 29px; width: 1067px; height: 824px;
    background: var(--ink);
    box-shadow: 8px 8px 10px rgba(0,0,0,.45);
    overflow: hidden;
    color: var(--paper);
  }
  .trifold-art { position: absolute; inset: 0; }

  /* Left panel – about */
  .about { position: absolute; left: 23px; top: 52px; width: 311px; }
  .about-title { font-weight: 600; font-size: 24px; line-height: 1.2; margin-bottom: 12px; }
  .about p {
    font-size: 13.1px; line-height: 18px; text-align: justify; hyphens: auto;
    margin-bottom: 18px;
  }
  .about .lead-in { display: block; font-weight: 700; }

  /* Middle panel */
  .tagline-quote {
    position: absolute; left: 408px; top: 266px; width: 250px;
    font-family: "Shadows Into Light", cursive;
    font-size: 27px; line-height: 38px; color: var(--soft-white);
    letter-spacing: .3px;
  }
  .quote-mark {
    font-family: Georgia, serif; color: var(--quote-mark); line-height: 1;
  }
  .quote-mark.open { position: absolute; left: 383px; top: 270px; font-size: 50px; }
  .quote-mark.close { font-size: 42px; vertical-align: -18px; margin-left: 2px; }

  .contact-card { position: absolute; left: 347px; top: 692px; width: 353px; text-align: center; }
  .performer-name { font-weight: 400; font-size: 23px; line-height: 1.2; }
  .performer-roles { font-weight: 700; font-size: 8.5px; letter-spacing: .2px; margin-top: 11px; }
  .phone {
    display: flex; align-items: center; justify-content: center; gap: 6px;
    font-weight: 700; font-size: 14px; margin-top: 9px;
  }
  .phone svg { width: 13px; height: 13px; }
  .site-small { font-size: 8.5px; font-weight: 600; margin-top: 7px; }

  /* Right panel */
  .role-stack {
    position: absolute; left: 700px; top: 52px; width: 367px; text-align: center;
    font-size: 21px; line-height: 32px; font-weight: 400; letter-spacing: .4px;
  }
  .site-large {
    position: absolute; left: 700px; top: 778px; width: 367px; text-align: center;
    font-size: 11.5px; font-weight: 600;
  }
</style>
</head>
<body>
<div class="stage-frame"></div>

<main class="trifold">
  <svg class="trifold-art" width="1067" height="824" viewBox="0 0 1067 824">
    <defs>
      <linearGradient id="mid-panel" x1="0" y1="0" x2="0" y2="1">
        <stop offset="0" stop-color="#262626"/>
        <stop offset=".6" stop-color="#1c1c1c"/>
        <stop offset="1" stop-color="#474747"/>
      </linearGradient>
      <pattern id="pinstripe" width="6" height="824" patternUnits="userSpaceOnUse">
        <rect width="3" height="824" fill="rgba(255,255,255,.025)"/>
      </pattern>
      <linearGradient id="swoosh" x1="0" y1="0" x2="1" y2="0">
        <stop offset="0" stop-color="#8d8d8d"/>
        <stop offset=".45" stop-color="#ffffff"/>
        <stop offset="1" stop-color="#d8d8d8"/>
      </linearGradient>
      <linearGradient id="stage-photo" x1="0" y1="0" x2="1" y2="1">
        <stop offset="0" stop-color="#141414"/>
        <stop offset=".5" stop-color="#2e2a28"/>
        <stop offset="1" stop-color="#121212"/>
      </linearGradient>
      <linearGradient id="closeup-photo" x1="0" y1="0" x2="1" y2="1">
        <stop offset="0" stop-color="#3a3a3a"/>
        <stop offset=".5" stop-color="#8a8a8a"/>
        <stop offset="1" stop-color="#4a4a4a"/>
      </linearGradient>
      <radialGradient id="portrait" cx=".5" cy=".45" r=".6">
        <stop offset="0" stop-color="#bdbdbd"/>
        <stop offset="1" stop-color="#6e6e6e"/>
      </radialGradient>
      <linearGradient id="lower-right" x1="0" y1="0" x2="1" y2="0">
        <stop offset="0" stop-color="#2e2e2e"/>
        <stop offset="1" stop-color="#0a0a0a"/>
      </linearGradient>
      <clipPath id="right-panel-clip">
        <rect x="700" y="0" width="367" height="824"/>
      </clipPath>
    </defs>

    <!-- middle panel base -->
    <rect x="347" y="0" width="353" height="824" fill="url(#mid-panel)"/>
    <rect x="347" y="0" width="353" height="824" fill="url(#pinstripe)"/>

    <!-- right panel stage photo -->
    <g role="img" aria-label="Photo: the performer on stage with a microphone, a young volunteer holding a prop beside a draped table">
      <rect x="700" y="160" width="367" height="560" fill="url(#stage-photo)"/>
    </g>

    <!-- top black cap over middle and right -->
    <path d="M347,0 H1067 V228 C920,220 820,190 700,172 C600,150 480,140 347,150 Z" fill="var(--ink)"/>
    <!-- top swoosh -->
    <path d="M347,132 C500,92 640,130 760,172 C870,205 980,214 1067,206 L1067,232 C960,236 860,214 760,190 C620,156 490,132 347,150 Z" fill="url(#swoosh)"/>

    <!-- lower right dark area under the bottom swoosh -->
    <g clip-path="url(#right-panel-clip)">
      <path d="M560,640 C680,712 880,715 1067,650 V824 H560 Z" fill="url(#lower-right)"/>
    </g>
    <!-- bottom swoosh, starting behind the portrait -->
    <path d="M560,628 C680,690 880,700 1067,622 L1067,650 C880,715 680,712 560,640 Z" fill="url(#swoosh)"/>

    <!-- left panel: black top, close-up photo, swoosh -->
    <rect x="0" y="0" width="347" height="824" fill="var(--ink)"/>
    <g role="img" aria-label="Photo: the performer doing close-up magic with cards for a guest">
      <rect x="0" y="560" width="347" height="264" fill="url(#closeup-photo)"/>
    </g>
    <path d="M0,0 H347 V548 C230,540 90,560 0,604 Z" fill="var(--ink)"/>
    <path d="M0,604 C90,560 230,540 347,548 L347,566 C230,558 100,578 0,630 Z" fill="url(#swoosh)"/>

    <!-- portrait circle -->
    <circle cx="521" cy="557" r="90" fill="#3c3c3c"/>
    <circle cx="521" cy="557" r="86" fill="var(--paper)"/>
    <g role="img" aria-label="Portrait photo of the performer">
      <circle cx="521" cy="557" r="80" fill="url(#portrait)"/>
    </g>
  </svg>

  <section class="about">
    <h1 class="about-title">About Wesley</h1>
    <p>From sleight-of-hand close-up magic with small objects like cards, coins, and dollar bills, mentalism, to stage illusions that can be seen by hundreds of people at a time, your guests will experience magic exquisitely performed by a master of his craft.</p>
    <p><span class="lead-in">I’m a professional entertainer.</span>I’ve been performing magic for over 40 years. I’ve been an Master of Ceremonies, Key Note Speaker (using magic during presentations to help build on a point or topic, while keeping the audience entertained and educated on the topic or topics the client has asked me to focus). I’ve performed all over the country for major corporations which means you’re getting tried and true, first-rate entertainment.</p>
    <p><span class="lead-in">My performances are guaranteed!</span>I pride myself on building relationships with my customers, so I’m not happy unless you’re happy. I guarantee your guests will have a great time and will thank you for having me there.</p>
  </section>

  <span class="quote-mark open" aria-hidden="true">“</span>
  <blockquote class="tagline-quote">If magic really existed, this is what it would look like.<span class="quote-mark close" aria-hidden="true">”</span></blockquote>

  <section class="contact-card">
    <h2 class="performer-name">Wesley Torvand</h2>
    <p class="performer-roles">MAGICIAN • MENTALIST • ENTERTAINER</p>
    <p class="phone">
      <svg viewBox="0 0 16 16" aria-hidden="true"><circle cx="8" cy="8" r="7" fill="none" stroke="#fff" stroke-width="1.4"/><path d="M5.4,4.2 L6.6,4 L7.3,5.8 L6.5,6.5 C7,7.6 8.2,8.9 9.4,9.5 L10.1,8.7 L11.9,9.4 L11.7,10.6 C9,11 5,7 5.4,4.2 Z" fill="#fff"/></svg>
      555 014 2290
    </p>
    <p class="site-small">www.wesleytorvandmagic.example</p>
  </section>

  <div class="role-stack">
    <p>MAGICIAN</p>
    <p>MENTALIST</p>
    <p>ENTERTAINER</p>
  </div>
  <p class="site-large">www.wesleytorvandmagic.example</p>
</main>
</body>
</html>
```